Classy business card for accounting firm

We're looking for a new business card for our accounting firm. Our logo was designed by Brandolith, so all of the design info we would like to use has been provided. The specific font provided isn't required to be used.

We want the card to look classy and elegent. Probably more minimalistic, but still with some pops of color.

The options we would like to include on the card are as follows:
1. Main office phone line
2. Direct phone line
3. Email address
4. Website URL
5. Name
6. Title (CEO, President, etc.)
7. Firm Address

The design and card should be double sided!!! The drop down box in the project brief for some reason is defaulting to single sided. Not sure why this is happening.

Thanks!

Contact Information for Business Card

The options we would like to include on the card are as follows: 1. Main office phone line 2. Direct phone line 3. Email address 4. Website URL 5. Name 6. Title (CEO, President, etc.) 7. Firm Address

Requirements
Must have
• Card must be double sided.

```html
<!DOCTYPE html>
<html lang="en">
<head>
<meta charset="utf-8">
<title>Ledgerline Associates – Business Card</title>
<link rel="stylesheet" href="https://fonts.googleapis.com/css2?family=Montserrat:wght@400;600;700&display=swap">
<style>
  :root {
    --stage: #1d1d1d;
    --lime: #bcc03a;
    --orange: #f47b20;
    --ink-grey: #636466;
    --paper: #ffffff;
    --card-w: 700px;
    --card-h: 400px;
  }
  * { box-sizing: border-box; margin: 0; padding: 0; }
  html, body {
    width: 1200px;
    height: 1189px;
    overflow: hidden;
    background: var(--stage);
    font-family: "Montserrat", sans-serif;
  }
  .sheet {
    width: 1200px;
    height: 1189px;
    display: flex;
    flex-direction: column;
    align-items: center;
    justify-content: center;
    gap: 90px;
  }
  .card {
    width: var(--card-w);
    height: var(--card-h);
    border-radius: 22px;
    position: relative;
    overflow: hidden;
  }

  /* Contact side */
  .card--contact {
    background: var(--lime);
    color: var(--paper);
  }
  .identity {
    position: absolute;
    left: 50px;
    top: 150px;
    width: 250px;
    text-align: right;
  }
  .identity__name {
    font-weight: 700;
    font-size: 27px;
    letter-spacing: 2px;
    line-height: 1.1;
  }
  .identity__title {
    font-weight: 400;
    font-size: 17px;
    letter-spacing: 0.5px;
    margin-top: 4px;
  }
  .divider {
    position: absolute;
    left: 332px;
    top: 130px;
    width: 1px;
    height: 140px;
    background: var(--paper);
  }
  .contact-list {
    position: absolute;
    left: 362px;
    top: 140px;
    list-style: none;
    font-size: 14.5px;
    font-weight: 400;
    line-height: 1.62;
    letter-spacing: 0.4px;
  }
  .contact-list b { font-weight: 700; }
  .contact-side__brand {
    position: absolute;
    right: 40px;
    top: 110px;
    font-weight: 600;
    font-size: 14px;
    letter-spacing: 1px;
  }

  /* Brand side */
  .card--brand {
    background: var(--paper);
    display: flex;
    align-items: center;
    justify-content: center;
    gap: 18px;
  }
  .brand__marker {
    width: 30px;
    height: 30px;
    background: var(--orange);
  }
  .brand__name {
    font-weight: 600;
    font-size: 38px;
    letter-spacing: 0.5px;
    color: var(--ink-grey);
  }
</style>
</head>
<body>
  <main class="sheet">
    <section class="card card--contact" aria-label="Card back with contact details">
      <div class="contact-side__brand">Ledgerline</div>
      <div class="identity">
        <h1 class="identity__name">DANIEL HART</h1>
        <p class="identity__title">CEO/President</p>
      </div>
      <div class="divider"></div>
      <ul class="contact-list">
        <li>Your Address, City,</li>
        <li>State, Country, Zip 12356</li>
        <li><b>P</b>. (555) 014-2890 (Main)</li>
        <li><b>P</b>. (555) 014-3370 (Direct)</li>
        <li><b>E</b>. info@ledgerlineassociates.com</li>
        <li><b>W</b>. ledgerlineassociates.com</li>
      </ul>
    </section>

    <section class="card card--brand" aria-label="Card front with firm name">
      <div class="brand__marker"></div>
      <h2 class="brand__name">Ledgerline Associates</h2>
    </section>
  </main>
</body>
</html>
```